The Perfect Business Card for PineHarbor

I am looking for a business card which beautifully incorporates my logo, reflects my business and looks special, elegant and clean.

```html
<!DOCTYPE html>
<html lang="en">
<head>
<meta charset="utf-8">
<title>PineHarbor Business Card</title>
<link rel="stylesheet" href="https://fonts.googleapis.com/css2?family=Cinzel:wght@400;600&family=Poppins:wght@400&display=swap">
<style>
  :root {
    --backdrop: #1d1d1d;
    --green-deep: #4f6e2a;
    --green-mid: #5f7f33;
    --green-light: #7a9c45;
    --paper: #ffffff;
    --ink-light: #ffffff;
    --brand-green: #557a2c;
  }
  * { margin: 0; padding: 0; box-sizing: border-box; }
  html, body { width: 1200px; height: 800px; overflow: hidden; background: var(--backdrop); }
  .canvas { position: relative; width: 1200px; height: 800px; }
  .card {
    position: absolute; width: 500px; height: 286px; border-radius: 16px; overflow: hidden;
    top: 257px;
  }
  .card-back { left: 70px; }
  .card-front { left: 630px; background: var(--paper); }

  .back-pattern {
    position: absolute; inset: 0;
    background: radial-gradient(ellipse at 45% 50%, var(--green-light) 0%, var(--green-mid) 45%, var(--green-deep) 100%);
  }
  .back-name {
    position: absolute; right: 34px; bottom: 40px;
    font-family: "Cinzel", serif; font-weight: 400; font-size: 13px; color: var(--ink-light);
  }

  .front-wave { position: absolute; inset: 0; }
  .brand-name {
    position: absolute; left: 44px; top: 78px;
    font-family: "Cinzel", serif; font-weight: 400; font-size: 30px; color: var(--brand-green);
  }
  .contact {
    position: absolute; right: 26px; top: 86px; text-align: right; color: var(--ink-light);
  }
  .contact-name { font-family: "Cinzel", serif; font-weight: 600; font-size: 17px; letter-spacing: 0.5px; }
  .contact-role { font-family: "Poppins", sans-serif; font-size: 10px; margin-bottom: 14px; }
  .contact-line {
    font-family: "Poppins", sans-serif; font-size: 10.5px; line-height: 15px;
    display: flex; justify-content: flex-end; align-items: center; gap: 6px;
  }
  .contact-line svg { width: 9px; height: 9px; fill: var(--ink-light); }
  .spacer { width: 9px; }
  .gap { height: 8px; }
</style>
</head>
<body>
<main class="canvas">
  <section class="card card-back">
    <div class="back-pattern" role="img" aria-label="Faint repeating brand pattern on green"></div>
    <span class="back-name">PineHarbor</span>
  </section>

  <section class="card card-front">
    <svg class="front-wave" viewBox="0 0 500 286" preserveAspectRatio="none" aria-hidden="true">
      <defs>
        <linearGradient id="waveGreen" x1="0" y1="1" x2="1" y2="0">
          <stop offset="0" stop-color="#5a7a30"/>
          <stop offset="0.55" stop-color="#799b44"/>
          <stop offset="1" stop-color="#557530"/>
        </linearGradient>
      </defs>
      <path d="M0,196 C40,252 110,282 180,250 C270,210 290,50 430,0 L500,0 L500,286 L0,286 Z" fill="#4c6b27"/>
      <path d="M0,202 C44,258 116,286 186,254 C276,214 296,54 438,0 L500,0 L500,286 L0,286 Z" fill="var(--paper)"/>
      <path d="M0,206 C48,262 122,290 192,258 C282,218 302,58 444,0 L500,0 L500,286 L0,286 Z" fill="url(#waveGreen)"/>
    </svg>

    <span class="brand-name">PineHarbor</span>

    <div class="contact">
      <div class="contact-name">Daniel Reyes</div>
      <div class="contact-role">President</div>
      <div class="contact-line">4120 Cedar Hollow Road<span class="spacer"></span></div>
      <div class="contact-line">Juneau, Alaska 99801<span class="spacer"></span></div>
      <div class="gap"></div>
      <div class="contact-line">555-240-7183
        <svg viewBox="0 0 10 10"><path d="M2 0.5 L3.6 2.6 L2.8 3.6 C3.4 5 4.6 6.3 6 7 L7 6.2 L9.4 7.8 L8.5 9.5 C4.5 9.3 0.7 5.5 0.5 1.5 Z"/></svg></div>
      <div class="contact-line">555-318-6402
        <svg viewBox="0 0 10 10"><path d="M2.5 0 H7.5 V10 H2.5 Z M3.3 1 V8.2 H6.7 V1 Z"/></svg></div>
      <div class="contact-line">name@pineharbor.com
        <svg viewBox="0 0 10 10"><path d="M0 2 H10 V8 H0 Z M0.8 2.6 L5 5.4 L9.2 2.6 Z" fill-rule="evenodd"/></svg></div>
      <div class="contact-line">www.pineharbor.com
        <svg viewBox="0 0 10 10"><circle cx="5" cy="5" r="4.6"/></svg></div>
    </div>
  </section>
</main>
</body>
</html>
```